Design a Website Mockup for a Car Website

Hi,

Thanks for your interest in this contest. I need a single page mockup for a vehicle website. The website hosts a web based application that enables users pull up vehicle specification data and history reports.
--
While the following communicate my requirements for the mockup, feel free to improve on them, not necessarily taking everything I've said into account.

As with most sites, the home page should be broken down into sections.

View of the home page from top to bottom:
First, our logo at the top left, a few links at the right (Register Stolen Vehicle | Find a Dealership) and a background image as well as a form field for the VIN.
See these sites for example background images: [login to view URL] [login to view URL] [login to view URL] [login to view URL]

You may choose to display the following texts anywhere on the home page:

"RoadVerra provides valuable information not readily available to you as a consumer, helping you make the right choices when purchasing your next car."
"RoadVerra helps you shop smart when buying a car."
"Harnessing the power of trusted automotive data, RoadVerra helps used car shoppers make safer investments."
"Knowledge is power. Start your used car search with a detailed specification report from RoadVerra."

Secondly, display a stacked, layered copy of the RoadVerra specification report. The report is available here: [login to view URL]

Use this or similar as a background behind the stacked reports: [login to view URL]

The stacked reports should be similar to these:

You may choose to display the following texts next to the stacked report images:

"Arm yourself with reliable vehicle specification data"

Does the car fit your needs, wants and lifestyle?
-- Discover seating and storage capacity, mechanical or performance specifications as well as any special considerations like weight, engine/transmission performance and fuel mileage to help narrow down your selection.

No Account Required, Easy Search
It's easy and straight forward. No Sign up, subscription or recurring fees. All you need is the vehicle indentification number (VIN) to get instant reports sent to you.

Car Research Made Easy
Every RoadVerra report includes a stolen database check. We routinely curate a list of stolen vehicles to protect unsuspecting buyers. You should also match the VIN and specifications data with the actual vehicle and registration documents to reveal the vehicle's characteristics are a match.

RoadVerra Vehicle History Reports
60% of all imported cars have bad history. Demand an RoadVerra Vehicle History report from the dealerships before committing financially.

Fourtly, we display testimonials. Great example: [login to view URL]

Fiftly, we display another field to perform the vin check and beside that, we can display a link to a sample report. Example: [login to view URL]

Sixtly, The footer.
--

UPDATE: 24/12/17

UPDATE: 25/12/17

```html
<!DOCTYPE html>
<html lang="en">
<head>
<meta charset="utf-8">
<title>RoadVerra – Research your next car</title>
<link rel="stylesheet" href="https://fonts.googleapis.com/css2?family=Fira+Sans:ital,wght@0,400;0,500;0,600;1,400&display=swap">
<style>
:root{
  --navy:#2d3557;
  --navy-deep:#283050;
  --orange:#ea861c;
  --orange-soft:#ec9a3f;
  --ink:#2f3650;
  --text:#5b5f6b;
  --muted:#8a8e99;
  --light:#f1f2f5;
  --white:#ffffff;
}
*{box-sizing:border-box;margin:0;padding:0}
html,body{width:1200px;height:2223px;overflow:hidden}
body{font-family:"Fira Sans",Arial,sans-serif;color:var(--text);background:var(--white);position:relative}
section,header,footer{position:relative;width:1200px;overflow:hidden}
.abs{position:absolute}
a{color:inherit;text-decoration:none}

/* Header */
.site-header{height:73px;background:var(--navy)}
.brand{left:173px;top:26px;display:flex;align-items:center;gap:8px;color:var(--white);font-size:26px;font-weight:600;letter-spacing:.2px}
.brand-dot{width:10px;height:10px;border-radius:50%;background:var(--orange)}
.nav-link{display:flex;align-items:center;gap:10px;color:var(--white);font-size:12.5px;line-height:15px;top:21px}
.nav-link svg{width:26px;height:26px}

/* Hero */
.hero{height:503px}
.hero-photo{inset:0;background:linear-gradient(100deg,#2f3a2f 0%,#51584d 30%,#7a2a2c 45%,#5b6160 65%,#8c938f 100%)}
.hero-shade{inset:0;background:linear-gradient(90deg,rgba(20,24,30,.55),rgba(20,24,30,.15) 60%,rgba(20,24,30,.1))}
.hero-title{left:171px;top:202px;color:var(--white);font-size:30px;font-weight:500}
.hero-lead{left:172px;top:248px;width:340px;color:var(--white);font-size:13px;line-height:20px}
.spec-card{left:745px;top:219px;width:271px;height:194px;background:#f4f4f4;box-shadow:0 0 0 8px rgba(255,255,255,.25);text-align:center}
.spec-card h2{margin-top:26px;font-size:18px;font-weight:500;color:var(--ink)}
.vin-input{display:block;margin:12px auto 0;width:210px;height:38px;border:1px solid #d7d8dc;background:var(--white);font:12.5px "Fira Sans",sans-serif;color:var(--muted);line-height:36px}
.vin-help{margin-top:11px;font-size:10px;color:var(--text)}
.btn-orange{display:inline-block;background:var(--orange);color:var(--white);font-size:11.5px;font-weight:600;text-transform:uppercase}
.spec-card .btn-orange{margin-top:10px;width:108px;height:36px;line-height:36px}

/* Intro strip */
.intro{height:75px;background:var(--white)}
.intro-thumb{left:233px;top:12px;width:98px;height:60px;background:linear-gradient(160deg,#e9ebf0,#c8ccd6);transform:skewY(-8deg)}
.intro-text{left:355px;top:26px;font-size:18px;color:var(--ink)}
.intro-text em{font-style:italic}
.btn-outline-orange{left:856px;top:19px;width:124px;height:37px;border:2px solid var(--orange);color:var(--orange);font-size:12px;display:flex;align-items:center;justify-content:center;gap:5px}

/* Buy / Sell */
.split{height:345px;display:flex}
.split-panel{position:relative;width:600px;height:345px;overflow:hidden}
.split-panel.buy{background:linear-gradient(120deg,#e8841b,#f09b3b 55%,#e3811a)}
.split-panel.sell{background:linear-gradient(120deg,#3d4770,#56608a 55%,#2f3860)}
.split-icon{position:absolute;top:726px;width:74px;height:74px;border:2px solid var(--white);border-radius:50%;display:flex;align-items:center;justify-content:center}
.split-body{position:absolute;top:72px;color:var(--white);width:300px}
.split-kicker{font-size:17px}
.split-title{font-size:29px;font-weight:500;line-height:34px}
.split-copy{margin-top:10px;font-size:12.5px;line-height:20px}
.btn-outline-white{margin-top:19px;width:123px;height:38px;border:2px solid var(--white);display:flex;align-items:center;justify-content:center;gap:5px;font-size:12px;text-transform:uppercase}

/* Benefits */
.benefits{height:355px;background:var(--light)}
.benefit{left:171px;display:flex;gap:14px;font-size:12.5px;line-height:20px;width:420px}
.benefit svg{flex:none;width:24px;height:24px;margin-top:1px}
.report-stack{left:647px;top:40px;width:420px;height:280px;background:linear-gradient(160deg,#fbfbfc,#dfe2e9 60%,#c9cdd8);clip-path:polygon(20% 20%,75% 0,100% 60%,45% 100%,0 70%)}

/* Pillars */
.pillars{height:352px;background:var(--white)}
.pillar{top:76px;width:220px;text-align:center}
.pillar svg{height:96px;width:110px}
.pillar h3{margin-top:22px;font-size:18px;font-weight:500;color:var(--ink)}
.pillar p{margin-top:12px;font-size:12.5px;line-height:20px}

/* CTA */
.cta{height:260px;background:var(--light);text-align:center}
.cta h2{position:absolute;top:54px;width:100%;font-size:32px;font-weight:400;color:var(--ink)}
.cta .vin-input{position:absolute;left:416px;top:110px;width:367px;height:36px;margin:0;text-align:left;padding-left:12px;line-height:34px}
.cta .btn-orange{position:absolute;left:549px;top:160px;width:108px;height:36px;line-height:36px}

/* Footer */
.site-footer{height:260px;background:var(--navy);color:var(--white)}
.foot-col{top:50px}
.foot-col h4{font-size:15px;font-weight:500;margin-bottom:8px}
.foot-col li{list-style:none;font-size:12.5px;line-height:22.5px;display:flex;align-items:center;gap:8px}
.social-dot{width:8px;height:8px;border-radius:50%;background:var(--white)}
.foot-col p{font-size:12.5px;line-height:19px;width:200px}
.email-field{margin-top:12px;width:197px;height:30px;background:var(--white);color:#555;font-size:12px;display:flex;align-items:center;justify-content:space-between;padding:0 8px 0 11px}
.email-go{width:18px;height:18px;border-radius:50%;background:var(--orange);display:flex;align-items:center;justify-content:center}
.legal{top:188px;font-size:12.5px}
</style>
</head>
<body>

<header class="site-header">
  <div class="brand abs"><span>RoadVerra</span><span class="brand-dot"></span></div>
  <a class="nav-link abs" style="left:793px" href="#">
    <svg viewBox="0 0 26 26" fill="none" stroke="#ea861c" stroke-width="2"><rect x="3" y="3" width="16" height="20" rx="1"/><path d="M7 9h8M7 13h8M7 17h5"/><path d="M15 20l7-7 2 2-7 7h-2z" fill="#ea861c"/></svg>
    <span>Register<br>Stolen Vehicle</span>
  </a>
  <a class="nav-link abs" style="left:936px" href="#">
    <svg viewBox="0 0 26 26" fill="none" stroke="#ea861c" stroke-width="2.4"><circle cx="11" cy="11" r="8"/><path d="M17 17l6 6"/><circle cx="11" cy="9" r="2.5" fill="#ea861c" stroke="none"/><path d="M6.5 15c1.5-2.5 7.5-2.5 9 0" stroke-width="2"/></svg>
    <span>Find a<br>Dealership</span>
  </a>
</header>

<section class="hero">
  <div class="hero-photo abs" role="img" aria-label="Red sedan on a mountain road with trees and cliffs behind"></div>
  <div class="hero-shade abs"></div>
  <h1 class="hero-title abs">Research your next car!</h1>
  <p class="hero-lead abs">Harnessing the power of trusted automotive data, RoadVerra™ helps used car shoppers and industry leaders make safer investments.</p>
  <form class="spec-card abs">
    <h2>Vehicle Specification</h2>
    <div class="vin-input">Enter Your Vin Number</div>
    <p class="vin-help">Where can I find the VIN?</p>
    <span class="btn-orange">Validate VIN</span>
  </form>
</section>

<section class="intro">
  <div class="intro-thumb abs" role="img" aria-label="Small stack of vehicle history reports"></div>
  <p class="intro-text abs">Introducing Vehicle History Reports - <em>Verify before you buy.</em></p>
  <a class="btn-outline-orange abs" href="#">LEARN MORE
    <svg width="14" height="10" viewBox="0 0 14 10" fill="none" stroke="currentColor" stroke-width="1.5"><path d="M0 5h12M8 1l4 4-4 4"/></svg></a>
</section>

<section class="split">
  <div class="split-panel buy" role="img" aria-label="Woman receiving car keys at a dealership, orange tint">
    <div class="split-icon" style="left:172px;top:72px">
      <svg width="40" height="32" viewBox="0 0 40 32" fill="#fff"><path d="M8 12l4-8h16l4 8h4v4h-2v12h-6v-4H12v4H6V16H4v-4zm5-1h14l-2.5-5h-9z"/><circle cx="11" cy="18" r="2.5" fill="#ea861c"/><circle cx="29" cy="18" r="2.5" fill="#ea861c"/></svg>
    </div>
    <div class="split-body" style="left:273px">
      <p class="split-kicker">Are You Looking To</p>
      <h2 class="split-title">Buy A Car?</h2>
      <p class="split-copy">Buy with confidence-RoadVerraTM provides reliable vehicle information. We tell you if a car has been reported stolen or has negative history. Contact your dealership for a detailed history report.</p>
      <a class="btn-outline-white" href="#">Learn More
        <svg width="14" height="10" viewBox="0 0 14 10" fill="none" stroke="#fff" stroke-width="1.5"><path d="M0 5h12M8 1l4 4-4 4"/></svg></a>
    </div>
  </div>
  <div class="split-panel sell" role="img" aria-label="Two men shaking hands beside a car, navy tint">
    <div class="split-icon" style="left:34px;top:72px">
      <svg width="30" height="44" viewBox="0 0 30 44" fill="none" stroke="#fff" stroke-width="5"><path d="M15 2v40"/><path d="M25 11c-2-3-6-4-10-4-5 0-9 2-9 7 0 10 19 5 19 15 0 5-4 7-10 7-4 0-8-1-10-4"/></svg>
    </div>
    <div class="split-body" style="left:135px">
      <p class="split-kicker">Do You Want To</p>
      <h2 class="split-title">Sell You Car?</h2>
      <p class="split-copy">Buy with confidence-RoadVerraTM provides reliable vehicle information. We tell you if a car has been reported stolen or has negative history. Contact your dealership for a detailed history report.</p>
      <a class="btn-outline-white" href="#">Learn More
        <svg width="14" height="10" viewBox="0 0 14 10" fill="none" stroke="#fff" stroke-width="1.5"><path d="M0 5h12M8 1l4 4-4 4"/></svg></a>
    </div>
  </div>
</section>

<section class="benefits">
  <div class="benefit abs" style="top:70px">
    <svg viewBox="0 0 24 24" fill="#ea861c"><rect x="1" y="7" width="22" height="15" rx="2"/><path d="M8 7V4h8v3" fill="none" stroke="#ea861c" stroke-width="2"/><rect x="1" y="13" width="22" height="1.5" fill="#fff"/></svg>
    <p>Comprehensive and consolidated vehicle infromation from. multiple authoritative sources</p>
  </div>
  <div class="benefit abs" style="top:129px">
    <svg viewBox="0 0 24 24" fill="#ea861c"><path d="M4 2h16v11c0 5-8 9-8 9s-8-4-8-9z"/><path d="M12 4h6v9c0 3-6 6-6 6z" fill="#fff"/></svg>
    <p>Checks include a stolen database check. Avoid costly mistakes With an instant RoadVerraTM VSR report</p>
  </div>
  <div class="benefit abs" style="top:188px">
    <svg viewBox="0 0 24 24"><circle cx="12" cy="12" r="11" fill="#ea861c"/><path d="M6.5 12.5l3.5 3.5 7.5-7.5" fill="none" stroke="#fff" stroke-width="2.4"/></svg>
    <p>Reliable and accurate data from Industry leaders to help you make informed decisions</p>
  </div>
  <div class="benefit abs" style="top:246px">
    <svg viewBox="0 0 24 24"><circle cx="12" cy="12" r="11" fill="#ea861c"/><text x="12" y="17" text-anchor="middle" fill="#fff" font-family="Fira Sans,sans-serif" font-weight="600" font-size="14">$</text></svg>
    <p>Value for your money. Shopping smart is guaranteed. We stay in business by giving you the best value you can find.</p>
  </div>
  <div class="report-stack abs" role="img" aria-label="Stacked, layered vehicle specification reports"></div>
</section>

<section class="pillars">
  <div class="pillar abs" style="left:197px">
    <svg viewBox="0 0 110 96">
      <circle cx="48" cy="42" r="38" fill="#fff" stroke="#2d3557" stroke-width="5"/>
      <path d="M74 70l22 22" stroke="#2d3557" stroke-width="8" stroke-linecap="round"/>
      <path d="M24 42l6-12h36l6 12h4v14h-6v6h-8v-6H34v6h-8v-6h-6V42zm9-2h30l-4-7H37z" fill="#2d3557"/>
      <circle cx="31" cy="48" r="3" fill="#fff"/><circle cx="65" cy="48" r="3" fill="#fff"/>
    </svg>
    <h3>Peace of mind</h3>
    <p>We source for detailed information and confirm vehicle specification and data.</p>
  </div>
  <div class="pillar abs" style="left:490px">
    <svg viewBox="0 0 110 96">
      <path d="M15 0h80v52c0 22-40 44-40 44S15 74 15 52z" fill="#2d3557"/>
      <path d="M55 8h32v44c0 15-32 34-32 34z" fill="#fff"/>
    </svg>
    <h3>Vehicle Theft</h3>
    <p>We regularly curate a list of stolen cars across Africa. All VSRs reflect the vehicle's status.</p>
  </div>
  <div class="pillar abs" style="left:782px">
    <svg viewBox="0 0 110 96" fill="#2d3557">
      <ellipse cx="55" cy="26" rx="20" ry="24"/>
      <path d="M20 96V74c0-10 10-18 22-20l13 18 13-18c12 2 22 10 22 20v22z"/>
      <path d="M51 62h8l-2 24-2 4-2-4z" fill="#fff"/>
    </svg>
    <h3>Dealerships</h3>
    <p>Certified dealerships enjoy access to a closed area with powerful tools to aid their business.</p>
  </div>
</section>

<section class="cta">
  <h2>Car research made easy</h2>
  <div class="vin-input">Enter Your Vehicle identification Number</div>
  <span class="btn-orange">Get Started</span>
</section>

<footer class="site-footer">
  <div class="foot-col abs" style="left:171px">
    <h4>Buyers</h4>
    <ul><li>What's in report?</li><li>Why buy a report?</li><li>View a sample report</li></ul>
  </div>
  <div class="foot-col abs" style="left:392px">
    <h4>Dealership</h4>
    <ul><li>Dealer Login</li><li>Register as a dealer</li><li>View a sample report</li></ul>
  </div>
  <div class="foot-col abs" style="left:611px">
    <h4>Connect with us</h4>
    <ul><li><span class="social-dot"></span>Friendwall</li><li><span class="social-dot"></span>Chirpline</li><li><span class="social-dot"></span>Worklink</li></ul>
  </div>
  <div class="foot-col abs" style="left:831px">
    <h4>Newsletter</h4>
    <p>Get industry news, blog and new features updates in your inbox.</p>
    <div class="email-field"><span>Email Address</span>
      <span class="email-go"><svg width="8" height="8" viewBox="0 0 8 8" fill="none" stroke="#fff" stroke-width="1.6"><path d="M2 1l3 3-3 3"/></svg></span></div>
  </div>
  <p class="legal abs" style="left:167px">Copyright ©2017 RoadVerra. All Rights Reserved.</p>
  <p class="legal abs" style="left:800px">Terms of Use | Privacy Policy | Sitemap</p>
</footer>

</body>
</html>
```